Harborline Network Solutions - IT Services Company/Managed Services/Consulting Card Design

Our company needs a business card design that will appeal to client companies with 50-1000 employees. We do IT services, administration, management, projects, budgeting and consulting (Like a small Quellbrook.com, Vantrelle.com or Drumvale.com). Mainly helping businesses use technology to be more competitive and efficient. We work with IT Infrastructure, switches, routers, firewalls and Cloud, Penwick/Tarvo servers, Kelpnode server virtualization, Datacenter environments, Email systems, Business Systems, Backup, Disaster Recovery, Data Security, ZPB, Workdesk 720 and Mistral.) Would like the final design to be professional but stand out to our prospective clients. Our current logo is attached. Color or design could be changed. Overall looking for a great finished product, original ideas are welcome and would pay more for the right one. If you think you have a better logo idea include a general idea if you can. Web design has not been done yet so that is a later possibility too.

Target Market(s)

1st - Mid-sized companies with 100-1000 employees with technology needs
2nd - Smaller companies with 20-99 employees with technology needs
- These companies can be in many different industries. Heathcare, legal, manufacturing, education, non-profit, services

Industry/Entity Type

Information Technology

Contact Information for Business Card

Should include the following info:

Logo or other logo with Company Name

Martin J. Calder

Principal

HarborlineNet.example

mcalder@HarborlineNet.example

(555) 7-HARBOR x 318

Font styles to use
Other font styles liked:
• designer can decide

Requirements
Must have
• Professional, appealing design, appeal to the target market
Nice to have
• Some sort of additional accent design that would stand out could be nice. I thought of adding a graphic in the top left corner that would look like the corner of the card was becoming more and more pixelated as it got near the corner, with some pixels missing.

```html
<!DOCTYPE html>
<html lang="en">
<head>
<meta charset="utf-8">
<title>Harborline Network Solutions – Business Card</title>
<link href="https://fonts.googleapis.com/css2?family=Montserrat:wght@400;600;700&display=swap" rel="stylesheet">
<style>
  :root {
    --bg: #e4e4e4;
    --card-light: #eeeeec;
    --card-dark: #302e2d;
    --accent-blue: #0b8fd3;
    --brand-navy: #1b2a52;
    --tag-blue: #1f5aa6;
    --text-light: #f2f2f2;
    --text-muted: #c9c9c9;
    --divider: #262423;
    --divider-hi: #3b3938;
  }
  * { box-sizing: border-box; margin: 0; padding: 0; }
  html, body {
    width: 1200px; height: 899px; overflow: hidden;
    background: var(--bg);
    font-family: "Montserrat", sans-serif;
  }
  .canvas {
    width: 1200px; height: 899px;
    display: flex; align-items: center; justify-content: center;
  }
  .business-card {
    position: relative;
    width: 1000px; height: 571px;
    background: var(--card-light);
    box-shadow: 0 18px 40px rgba(0,0,0,0.18);
    overflow: hidden;
  }
  .accent-band {
    height: 24px;
    background: var(--accent-blue);
  }
  .brand-block {
    position: absolute;
    left: 190px; top: 100px;
  }
  .brand-name {
    font-weight: 700;
    font-size: 44px;
    letter-spacing: 1px;
    color: var(--brand-navy);
    text-transform: uppercase;
    line-height: 1.05;
  }
  .brand-tagline {
    margin-top: 14px;
    padding-top: 8px;
    border-top: 2px solid var(--tag-blue);
    font-weight: 600;
    font-size: 17px;
    letter-spacing: 3px;
    color: var(--tag-blue);
    text-transform: uppercase;
  }
  .contact-panel {
    position: absolute;
    left: 0; right: 0; bottom: 0;
    height: 300px;
    background: var(--card-dark);
  }
  .row-divider {
    position: absolute;
    left: 0; right: 0; top: 148px;
    height: 2px;
    background: var(--divider);
    border-bottom: 1px solid var(--divider-hi);
  }
  .contact-item {
    position: absolute;
    display: flex; align-items: center; gap: 16px;
    height: 60px;
    color: var(--text-light);
    font-size: 22px;
    white-space: nowrap;
  }
  .contact-icon {
    width: 50px; height: 50px; flex: none;
  }
  .person-name {
    font-weight: 700; font-size: 24px; letter-spacing: 0.5px;
    text-transform: uppercase; line-height: 1.05;
  }
  .person-title { color: var(--text-muted); font-size: 21px; }
  .item-person { left: 90px;  top: 44px; }
  .item-phone  { left: 520px; top: 44px; }
  .item-web    { left: 90px;  top: 194px; }
  .item-email  { left: 520px; top: 194px; }
</style>
</head>
<body>
<main class="canvas">
  <section class="business-card" aria-label="Business card for Harborline Network Solutions">
    <div class="accent-band"></div>

    <div class="brand-block">
      <div class="brand-name">Harborline<br>Network Solutions</div>
      <div class="brand-tagline">Connected. Secure. Efficient.</div>
    </div>

    <div class="contact-panel">
      <div class="row-divider"></div>

      <div class="contact-item item-person">
        <svg class="contact-icon" viewBox="0 0 50 50" aria-hidden="true">
          <circle cx="25" cy="25" r="22" fill="#fff" stroke="var(--accent-blue)" stroke-width="4"/>
          <circle cx="25" cy="20" r="6" fill="var(--card-dark)"/>
          <path d="M14 35 q11 -13 22 0 z" fill="var(--card-dark)"/>
        </svg>
        <div>
          <div class="person-name">Martin J. Calder</div>
          <div class="person-title">Principal</div>
        </div>
      </div>

      <div class="contact-item item-phone">
        <svg class="contact-icon" viewBox="0 0 50 50" aria-hidden="true">
          <circle cx="25" cy="25" r="22" fill="#fff" stroke="var(--accent-blue)" stroke-width="4"/>
          <path d="M14 22 q11 -9 22 0 l-3 4 h-4 v-3 h-8 v3 h-4 z" fill="var(--card-dark)"/>
          <rect x="17" y="27" width="16" height="8" rx="2" fill="var(--card-dark)"/>
        </svg>
        <span>(555) 7-HARBOR x 318</span>
      </div>

      <div class="contact-item item-web">
        <svg class="contact-icon" viewBox="0 0 50 50" aria-hidden="true">
          <circle cx="25" cy="25" r="22" fill="#fff" stroke="var(--accent-blue)" stroke-width="4"/>
          <circle cx="25" cy="25" r="11" fill="none" stroke="var(--card-dark)" stroke-width="2.5"/>
          <ellipse cx="25" cy="25" rx="5" ry="11" fill="none" stroke="var(--card-dark)" stroke-width="2"/>
          <line x1="14" y1="25" x2="36" y2="25" stroke="var(--card-dark)" stroke-width="2"/>
        </svg>
        <span>HarborlineNet.example</span>
      </div>

      <div class="contact-item item-email">
        <svg class="contact-icon" viewBox="0 0 50 50" aria-hidden="true">
          <circle cx="25" cy="25" r="22" fill="#fff" stroke="var(--accent-blue)" stroke-width="4"/>
          <rect x="14" y="18" width="22" height="15" fill="none" stroke="var(--card-dark)" stroke-width="2.2"/>
          <polyline points="14,18 25,27 36,18" fill="none" stroke="var(--card-dark)" stroke-width="2.2"/>
        </svg>
        <span>mcalder@HarborlineNet.example</span>
      </div>
    </div>
  </section>
</main>
</body>
</html>
```